Real Estate agent needs flyer/folder to contain bio and overview of services

I'm including files of the layout of the small folder. The folder is 6 1/2 across and 9 1/2 inches long. It will have a front & back cover and then writing on the 2 inside pages.

I am sending a few files to incorporate into the flyer, 1 new logo to use and 2 files which are coloring ideas.

```html
<!DOCTYPE html>
<html lang="en">
<head>
<meta charset="utf-8">
<title>Marla Devereaux – Realtor Folder</title>
<link href="https://fonts.googleapis.com/css2?family=Montserrat:wght@400;500;600;700&family=Open+Sans:wght@400;600&display=swap" rel="stylesheet">
<style>
  :root{
    --blue:#2b51b0;
    --blue-dark:#1d3a86;
    --blue-light:#4a74d4;
    --grey-bg:#e4e6ea;
    --page-grey:#eceef1;
    --silver-light:#f7f8fa;
    --silver-mid:#dfe2e7;
    --ink:#3c4150;
    --badge:#d6322e;
    --white:#ffffff;
  }
  *{box-sizing:border-box;margin:0;padding:0}
  html,body{width:1200px;height:2316px;overflow:hidden}
  body{background:var(--grey-bg);font-family:"Open Sans",Arial,sans-serif;color:var(--ink);position:relative}

  .page-label{position:absolute;font-family:"Montserrat",Arial,sans-serif;font-size:18px;font-weight:500;color:#33363d;text-align:center;width:540px}
  .page{position:absolute;width:540px;height:789px;overflow:hidden;background:var(--page-grey);box-shadow:0 8px 24px rgba(0,0,0,.18)}
  .page svg.bg{position:absolute;inset:0;width:100%;height:100%}

  .silver-texture{position:absolute;left:0;top:0;width:100%;height:640px;
    background:linear-gradient(150deg,var(--silver-light) 0%,var(--silver-mid) 45%,var(--silver-light) 70%,var(--page-grey) 100%)}

  .cover-front{left:40px;top:330px}
  .cover-back{left:620px;top:330px}
  .spread{position:absolute;left:60px;top:1200px;width:1080px;height:789px;box-shadow:0 8px 24px rgba(0,0,0,.18)}
  .spread .page{box-shadow:none;top:0}
  .inside-left{left:0}
  .inside-right{left:540px;background:var(--blue)}

  .brand{position:absolute;left:0;width:100%;text-align:center;font-family:"Montserrat",Arial,sans-serif;font-weight:600;color:var(--blue);letter-spacing:1px}
  .brand-dot{display:inline-block;width:14px;height:14px;border-radius:50%;background:var(--blue);margin-right:12px;vertical-align:middle}
  .tagline{position:absolute;width:100%;text-align:center;font-family:"Montserrat",Arial,sans-serif;font-weight:600;color:var(--blue);letter-spacing:1.5px}
  .website{position:absolute;width:100%;text-align:center;font-family:"Montserrat",Arial,sans-serif;font-size:11px;letter-spacing:2px;color:var(--ink)}
  .badge{position:absolute;background:var(--badge);border-radius:3px}

  .contact{position:absolute;left:150px;top:430px;font-size:11px;line-height:18px;color:var(--ink)}
  .contact .name{font-family:"Montserrat",Arial,sans-serif;font-weight:700;font-size:12px;color:var(--blue);letter-spacing:1px}
  .contact-line{display:flex;align-items:center;gap:6px}
  .contact-line svg{width:10px;height:10px;fill:var(--blue)}
  .agent-photo{position:absolute;left:80px;top:428px;width:60px;height:60px;border-radius:50%;background:linear-gradient(160deg,#9db2d8,#4b5f86);border:3px solid var(--white)}
  .affil-mark{position:absolute;width:22px;height:22px;border:2px solid var(--white);border-radius:3px}

  .house-photo{position:absolute;left:0;top:0;width:200px;height:789px;background:linear-gradient(180deg,#c7a6bd 0%,#e2b7a8 30%,#9a7a64 55%,#6b5a45 72%,#5d7a3e 88%,#4e6a34 100%)}
  .bio-column{position:absolute;left:218px;top:120px;width:300px}
  .bio-brand{position:absolute;left:200px;top:30px;width:340px;text-align:center;font-family:"Montserrat",Arial,sans-serif;font-weight:600;color:var(--blue);font-size:22px;letter-spacing:1px}
  .section-title{font-family:"Montserrat",Arial,sans-serif;font-weight:700;font-size:14px;color:var(--blue);margin:14px 0 6px}
  .body-copy{font-size:10px;line-height:15px;margin-bottom:7px;color:var(--ink)}
  .bio-column .body-copy{text-align:justify}

  .services-column{position:absolute;left:36px;top:40px;width:468px;color:var(--white)}
  .services-column .section-title{color:var(--white);font-size:13px;letter-spacing:1.5px;margin:22px 0 8px;text-transform:uppercase}
  .services-column .body-copy{color:#e6ecfa;font-size:10px;line-height:15px}
  .testimonial-by{font-family:"Montserrat",Arial,sans-serif;font-weight:600;font-size:10px;color:var(--white);margin:-2px 0 12px}
</style>
</head>
<body>

<div class="page-label" style="left:40px;top:290px">Front Page</div>
<div class="page-label" style="left:620px;top:290px">Back Page</div>

<!-- Front cover -->
<section class="page cover-front">
  <div class="silver-texture" role="img" aria-label="Silver geometric background pattern"></div>
  <svg class="bg" viewBox="0 0 540 789" preserveAspectRatio="none">
    <defs>
      <linearGradient id="fBlue" x1="0" y1="0" x2="0" y2="1">
        <stop offset="0" stop-color="#3a62c6"/><stop offset="1" stop-color="#1d3a86"/>
      </linearGradient>
    </defs>
    <path d="M470,0 C430,220 500,420 540,470 L540,0 Z" fill="url(#fBlue)"/>
    <path d="M0,640 C160,600 360,620 540,560 L540,789 L0,789 Z" fill="var(--blue-light)" opacity=".7"/>
    <path d="M0,680 C180,650 380,670 540,610 L540,789 L0,789 Z" fill="url(#fBlue)"/>
  </svg>
  <div class="brand" style="top:270px;font-size:32px"><span class="brand-dot"></span>Marla Devereaux</div>
  <div class="tagline" style="top:470px;font-size:15px">FINE HOMES &amp; LUXURY PROPERTIES</div>
  <div class="website" style="top:500px">www.marladsells.com</div>
  <div class="badge" style="left:30px;top:742px;width:40px;height:20px"></div>
</section>

<!-- Back cover -->
<section class="page cover-back">
  <div class="silver-texture" role="img" aria-label="Silver geometric background pattern"></div>
  <svg class="bg" viewBox="0 0 540 789" preserveAspectRatio="none">
    <defs>
      <linearGradient id="bBlue" x1="0" y1="0" x2="0" y2="1">
        <stop offset="0" stop-color="#3a62c6"/><stop offset="1" stop-color="#1d3a86"/>
      </linearGradient>
    </defs>
    <path d="M70,0 C110,220 40,420 0,470 L0,0 Z" fill="url(#bBlue)"/>
    <path d="M0,620 C180,660 380,640 540,600 L540,789 L0,789 Z" fill="var(--blue-light)" opacity=".7"/>
    <path d="M0,670 C180,700 380,680 540,650 L540,789 L0,789 Z" fill="url(#bBlue)"/>
  </svg>
  <div class="brand" style="top:230px;font-size:28px"><span class="brand-dot"></span>Marla Devereaux</div>
  <div class="agent-photo" role="img" aria-label="Portrait photo of the agent"></div>
  <div class="contact">
    <div class="name">MARLA DEVEREAUX</div>
    <div class="contact-line"><svg viewBox="0 0 10 10"><path d="M2 0h2l1 3-1.5 1a6 6 0 0 0 2.5 2.5L7 5l3 1v2a2 2 0 0 1-2 2A8 8 0 0 1 0 2a2 2 0 0 1 2-2z"/></svg>(555) 013-2748</div>
    <div class="contact-line"><svg viewBox="0 0 10 10"><path d="M2 0h2l1 3-1.5 1a6 6 0 0 0 2.5 2.5L7 5l3 1v2a2 2 0 0 1-2 2A8 8 0 0 1 0 2a2 2 0 0 1 2-2z"/></svg>(555) 013-9061</div>
    <div class="contact-line"><svg viewBox="0 0 10 10"><path d="M0 2h10v6H0z M0 2l5 3 5-3" fill="none" stroke="var(--blue)" stroke-width="1.2"/></svg>marla@marladsells.com</div>
  </div>
  <div class="badge" style="left:30px;top:742px;width:40px;height:20px"></div>
  <div class="affil-mark" style="left:444px;top:740px"></div>
  <div class="affil-mark" style="left:476px;top:740px"></div>
</section>

<!-- Inside spread -->
<div class="spread">
  <section class="page inside-left" style="background:var(--white)">
    <div class="house-photo" role="img" aria-label="Photo of a stone family home at sunset"></div>
    <svg class="bg" viewBox="0 0 540 789" preserveAspectRatio="none" style="pointer-events:none">
      <path d="M200,745 C300,735 420,750 540,730 L540,789 L200,789 Z" fill="var(--blue)"/>
    </svg>
    <div class="bio-brand"><span class="brand-dot" style="width:10px;height:10px;margin-right:8px"></span>Marla Devereaux</div>
    <div class="bio-column">
      <h2 class="section-title">Let me Introduce Myself</h2>
      <p class="body-copy">I have called this region home for over twenty years, and helping families find the right address is the work I love most. I bring local insight, steady communication and honest advice to every move.</p>
      <p class="body-copy">Whether you are buying your first home or selling a cherished property, I guide each step with care, from pricing and staging to closing day and beyond.</p>
      <h2 class="section-title">My Core Team</h2>
      <p class="body-copy">Behind every sale stands a trusted group of lenders, inspectors, stagers and attorneys who share my standards and keep your transaction on track.</p>
      <h2 class="section-title">Real Estate Services &amp; Beyond...</h2>
      <p class="body-copy">From market reports and home valuations to relocation support and vendor referrals, I offer resources that make every chapter of homeownership easier.</p>
    </div>
    <div class="website" style="left:200px;width:340px;top:712px">www.marladsells.com</div>
  </section>

  <section class="page inside-right">
    <svg class="bg" viewBox="0 0 540 789" preserveAspectRatio="none">
      <defs>
        <linearGradient id="rBlue" x1="0" y1="0" x2="1" y2="1">
          <stop offset="0" stop-color="#3459bd"/><stop offset="1" stop-color="#1d3a86"/>
        </linearGradient>
      </defs>
      <rect width="540" height="789" fill="url(#rBlue)"/>
    </svg>
    <div class="services-column">
      <h2 class="section-title" style="margin-top:0">Selling Your Home</h2>
      <p class="body-copy">A successful sale starts with the right strategy. I prepare a detailed market analysis, recommend smart improvements and price your home to attract serious buyers.</p>
      <p class="body-copy">Professional photography, targeted online marketing and open houses put your property in front of the right audience, while I negotiate firmly on your behalf.</p>
      <h2 class="section-title">Buying a Home</h2>
      <p class="body-copy">I listen closely to your needs, arrange private showings and share honest insight on every neighborhood so you can choose with confidence.</p>
      <p class="body-copy">When you find the one, I write a strong offer, coordinate inspections and keep every deadline clear until the keys are in your hand.</p>
      <h2 class="section-title">Testimonials</h2>
      <p class="body-copy">“Marla made our sale simple and stress free. Her advice on pricing was spot on and we closed in three weeks.”</p>
      <p class="testimonial-by">— Peter &amp; Anne Holloway</p>
      <p class="body-copy">“Patient, knowledgeable and always reachable. We found our dream home thanks to her.”</p>
      <p class="testimonial-by">— Daniel Okafor</p>
    </div>
  </section>
</div>

</body>
</html>
```